Business Card Design

I need a business card design for a new company based in Australind, Western Australia. The business is for puppet shows at children's parties, fetes, custom puppet builds, etc.Attached is a picture of Ray Caldwick in silhouette. I was thinking a design of a puppeteer at the top of some stairs talking to a puppet in silhouette but open to suggestions. (Under the willow is named as I do all my puppet builds in the top room of my house (at the Under the willow).

Industry/Entity Type

Business

Contact Information for Business Card

Under The Willow Puppets, Dale Munroe, Puppeteer / Puppet Builder, phone - 0438215076, Puppet shows / Custom Puppet Builds, Working With Children

Requirements
Must have
• Name and Logo on one side. Second side to have business card details.

```html
<!DOCTYPE html>
<html lang="en">
<head>
<meta charset="utf-8">
<title>Under The Willow Puppets – Business Card</title>
<link href="https://fonts.googleapis.com/css2?family=Questrial&display=swap" rel="stylesheet">
<style>
  :root {
    --backdrop: #1b2030;
    --crimson-deep: #8c0f20;
    --crimson-light: #b8405a;
    --crimson: #9e1428;
    --ink: #141414;
    --paper: #ffffff;
    --swoosh: #1a1a1a;
  }
  * { margin: 0; padding: 0; box-sizing: border-box; }
  html, body {
    width: 1200px; height: 900px; overflow: hidden;
    background: var(--backdrop);
    font-family: "Questrial", "Century Gothic", sans-serif;
  }
  .sheet {
    position: relative; width: 1200px; height: 900px;
    display: flex; flex-direction: column; align-items: center; justify-content: center; gap: 40px;
  }
  .card {
    position: relative; width: 700px; height: 400px;
    border-radius: 24px; overflow: hidden;
    box-shadow: 0 14px 30px rgba(0,0,0,0.55);
  }
  /* Front */
  .card--front {
    background: linear-gradient(100deg, var(--crimson-deep) 0%, var(--crimson) 45%, var(--crimson-light) 100%);
    display: flex; align-items: center; justify-content: center;
  }
  .brand { display: flex; align-items: center; gap: 14px; }
  .brand__mark { width: 40px; height: 40px; }
  .brand__name { font-size: 36px; line-height: 1; white-space: nowrap; }
  .card--front .brand__mark { background: var(--paper); }
  .card--front .brand__name { color: var(--paper); }
  /* Back */
  .card--back { background: var(--paper); }
  .card--back .brand {
    position: absolute; top: 48px; right: 40px; gap: 10px;
  }
  .card--back .brand__mark { width: 30px; height: 30px; background: var(--crimson); }
  .card--back .brand__name { color: var(--ink); font-size: 24px; }
  .contact { position: absolute; left: 44px; top: 150px; }
  .contact__name { font-size: 42px; color: var(--ink); line-height: 1.1; }
  .contact__role { font-size: 22px; color: var(--crimson); margin-top: 4px; }
  .contact__line {
    display: flex; align-items: center; gap: 14px;
    font-size: 24px; color: var(--ink); margin-top: 10px;
  }
  .contact__line:first-of-type { margin-top: 14px; }
  .contact__icon { width: 26px; height: 22px; flex: none; }
  .swoosh { position: absolute; left: 0; top: 0; width: 700px; height: 400px; }
  .services {
    position: absolute; left: 30px; bottom: 22px;
    font-size: 21px; color: var(--paper); letter-spacing: 0.3px;
  }
</style>
</head>
<body>
<main class="sheet">
  <section class="card card--front" aria-label="Card front">
    <div class="brand">
      <span class="brand__mark"></span>
      <span class="brand__name">Under The Willow Puppets</span>
    </div>
  </section>

  <section class="card card--back" aria-label="Card back">
    <svg class="swoosh" viewBox="0 0 700 400" aria-hidden="true">
      <defs>
        <linearGradient id="bandFill" x1="0" y1="0" x2="1" y2="0">
          <stop offset="0" stop-color="#8c0f20"/>
          <stop offset="0.5" stop-color="#9e1428"/>
          <stop offset="1" stop-color="#b8405a"/>
        </linearGradient>
      </defs>
      <path d="M0,300 C150,330 380,300 540,240 C610,214 660,196 700,190 L700,205 C600,230 420,330 0,345 Z" fill="var(--swoosh)"/>
      <path d="M0,340 C200,345 420,310 560,250 C620,225 665,210 700,205 L700,400 L0,400 Z" fill="url(#bandFill)"/>
      <path d="M0,336 C210,340 420,306 560,246 C620,221 665,206 700,201" fill="none" stroke="#ffffff" stroke-width="3"/>
    </svg>

    <div class="brand">
      <span class="brand__mark"></span>
      <span class="brand__name">Under The Willow Puppets</span>
    </div>

    <div class="contact">
      <p class="contact__name">Dale Munroe,</p>
      <p class="contact__role">Puppeteer / Puppet Builder</p>
      <p class="contact__line">
        <svg class="contact__icon" viewBox="0 0 26 22" aria-hidden="true">
          <path d="M1,7 C1,2 25,2 25,7 L25,9 L19,9 L19,6 L7,6 L7,9 L1,9 Z" fill="var(--crimson)"/>
          <path d="M5,11 L9,8 L17,8 L21,11 L23,21 L3,21 Z" fill="var(--crimson)"/>
          <circle cx="13" cy="15" r="3" fill="#fff"/>
        </svg>
        <span>0438215076</span>
      </p>
      <p class="contact__line">
        <svg class="contact__icon" viewBox="0 0 26 22" aria-hidden="true">
          <rect x="1" y="3" width="24" height="16" fill="var(--crimson)"/>
          <path d="M1,3 L13,12 L25,3" fill="none" stroke="#fff" stroke-width="1.6"/>
        </svg>
        <span>hello@willowpuppets.com</span>
      </p>
    </div>

    <p class="services">Puppet shows, Children's parties, Custom puppet builds</p>
  </section>
</main>
</body>
</html>
```